Meadowlark Cleaning Services - Redesign

I've got my website designed a few years ago and it looks dated now. I would like to get a modern, happy, bright, and clean look. All the content needed can be found at my current website www.meadowlarkcs.example. Not necessarily need to use all of it, since I want something more clean and easy to read.
I need a 5 pages website:
HOME | SERVICES | ESTIMATE |TESTIMONIALS | CONTACT US

Industry/Entity Type

Janitorial Service

Number of Pages Required

5+ page

Colors
0792cd
34a6d7
85cae6
cee9f5
ebebeb
f0f0f0
f5f5f5
b1b1b1
000000

Requirements
Must have
• Who we are?
• Meadowlark Cleaning Services is a local, family-owned, client-focused house and office cleaning company that strives to ensure the highest level of customer satisfaction. We offer expert residential and commercial cleaning services to all the Seattle and Eastside areas.
• Why Meadowlark?
• √ We are insured, bonded and licensed.
•  Meadowlark Cleaning Service is Fully Insured so you can rest easy knowing your home is protected.
•  Copy of insurance available upon request.
•

√ We provide all supplies and equipments needed to thoroughly clean your home or business.

• √ We are not a franchise. We are a local, family-owned company.

• When you call Meadowlark Cleaning Services, you’ll always speak to one of the owners, which is a great benefit to you since this allows us to give you the personal attention and more time needed to clean your home the way you want it cleaned.

• √ We are good at what we do, and we like doing it.

```html
<!DOCTYPE html>
<html lang="en">
<head>
<meta charset="utf-8">
<title>Meadowlark Cleaning Services</title>
<link href="https://fonts.googleapis.com/css2?family=Oswald:wght@400;500&family=Lato:ital,wght@0,400;0,700;1,400&display=swap" rel="stylesheet">
<style>
:root{
  --blue:#0792cd;
  --blue-mid:#34a6d7;
  --blue-light:#85cae6;
  --blue-pale:#cee9f5;
  --grey-1:#ebebeb;
  --grey-2:#f0f0f0;
  --grey-3:#f5f5f5;
  --grey-4:#b1b1b1;
  --black:#000;
  --ink:#222;
  --text:#555;
  --footer:#1f1f1f;
  --footer-bar:#333;
}
*{box-sizing:border-box;margin:0;padding:0}
html,body{width:1200px;height:2192px;overflow:hidden}
body{position:relative;font-family:'Lato',sans-serif;color:var(--text);background:#fff}
.abs{position:absolute}
.oswald{font-family:'Oswald',sans-serif}

/* top bar */
.topbar{left:0;top:0;width:1200px;height:39px;border-bottom:1px solid var(--grey-1);background:#fff}
.topbar .contact{top:10px;font-size:14px;color:var(--ink);display:flex;align-items:center;gap:8px}
.quote-btn{left:933px;top:0;width:135px;height:39px;background:var(--black);color:#fff;font-family:'Oswald',sans-serif;font-size:16px;display:flex;align-items:center;justify-content:center}

/* header */
.brand{left:134px;top:66px;font-size:42px;font-weight:700;color:var(--blue);letter-spacing:-0.5px}
.social{width:38px;height:38px;border:2px solid var(--blue);border-radius:50%;top:76px}

/* nav */
.nav{left:0;top:149px;width:1200px;height:47px;background:var(--blue)}
.nav::before{content:"";position:absolute;left:0;top:0;width:100%;height:12px;background:var(--blue-mid)}
.nav-item{top:0;height:47px;display:flex;align-items:center;justify-content:center;color:#fff;font-family:'Oswald',sans-serif;font-size:16px;text-transform:uppercase}
.nav-item.active{background:var(--black)}
.nav-div{top:0;width:1px;height:47px;background:rgba(255,255,255,.25)}

/* hero */
.hero{left:0;top:196px;width:1200px;height:517px;background:linear-gradient(100deg,#d9d6d2 0%,#eeeae6 35%,#f4f1ed 55%,#d6cfc6 80%,#bdb6ad 100%)}
.hero-caption{left:132px;top:341px;width:447px;height:171px;background:rgba(255,255,255,.85);padding:10px 20px}
.hero-caption h1{font-size:28px;font-weight:400;line-height:42px;color:var(--ink)}
.dots{position:absolute;left:20px;bottom:18px;display:flex;gap:5px}
.dots span{width:7px;height:7px;border-radius:50%;background:var(--grey-4)}
.dots span.on{background:var(--blue)}

/* welcome */
.welcome{left:0;top:713px;width:1200px;height:325px;background:var(--blue);color:#fff}
.welcome h2{position:absolute;left:136px;top:37px;font-family:'Oswald',sans-serif;font-weight:400;font-size:30px}
.welcome .rule{position:absolute;left:132px;top:88px;width:657px;height:1px;background:rgba(255,255,255,.35)}
.welcome .rule::before{content:"";position:absolute;left:0;top:-5px;width:10px;height:10px;border:1px solid rgba(255,255,255,.5);border-radius:50%;background:var(--blue)}
.welcome p{position:absolute;left:132px;top:110px;width:660px;font-size:14.5px;line-height:22px}
.read-more{position:absolute;left:132px;top:244px;width:109px;height:36px;border:2px solid #fff;border-radius:6px;display:flex;align-items:center;justify-content:center;font-family:'Oswald',sans-serif;font-size:16px}
.seal{position:absolute;left:843px;top:49px}

/* sections */
.section-title{width:1200px;left:0;text-align:center;font-family:'Oswald',sans-serif;font-weight:400;font-size:30px;color:var(--blue)}
.center-rule{height:1px;background:#d5d5d5}
.center-rule::after{content:"";position:absolute;left:50%;top:-5px;margin-left:-5px;width:10px;height:10px;border-radius:50%;border:1px solid var(--grey-4);background:#fff}

.services{left:0;top:1038px;width:1200px;height:487px;background:var(--grey-2)}
.svc-icon{width:74px;height:74px;border-radius:50%;background:#2a2a2a;box-shadow:0 0 0 3px #d8d8d8;display:flex;align-items:center;justify-content:center}
.svc-title{font-family:'Oswald',sans-serif;font-size:23px;color:var(--ink)}
.svc-desc{font-size:14.5px;line-height:19px;color:var(--text);width:310px}

/* testimonials */
.card{top:1710px;width:289px;height:154px;background:#fff;border:1px solid var(--grey-1);box-shadow:0 1px 3px rgba(0,0,0,.12);text-align:center;padding:28px 22px 0}
.card h4{font-family:'Oswald',sans-serif;font-weight:400;font-size:14px;color:var(--ink);margin-bottom:8px}
.card p{font-style:italic;font-size:12px;line-height:20px;color:var(--text)}
.avatar{top:1663px;width:64px;height:64px;border-radius:50%;border:2px solid var(--blue);background:linear-gradient(#e8e8e8,#9a9a9a)}
.arrow{top:1770px;width:36px;height:36px;border-radius:50%;background:#fff;box-shadow:0 1px 4px rgba(0,0,0,.2);display:flex;align-items:center;justify-content:center}

/* footer */
.footer{left:0;top:1929px;width:1200px;height:220px;background:var(--footer);color:#ddd}
.f-head{top:20px;font-family:'Oswald',sans-serif;font-size:18px;color:#fff;padding-bottom:8px;border-bottom:1px solid #444}
.f-links{top:62px;left:133px;list-style:none;font-size:14px;line-height:29.5px}
.f-links li::before{content:"›";margin-right:8px;color:#aaa}
.f-line{font-size:13px;display:flex;gap:12px}
.f-sep{top:20px;width:1px;height:180px;background:#3a3a3a}
.map{left:583px;top:63px;width:202px;height:126px;border:3px solid #fff;background:linear-gradient(135deg,#e9e4d6,#d8e6c8 60%,#c9dcef)}
.f-brand{left:890px;top:108px;font-size:40px;font-weight:700;color:#8a8a8a}
.bottombar{left:0;top:2149px;width:1200px;height:43px;background:var(--footer-bar);color:#eee;font-size:14px}
.f-social{top:9px;width:27px;height:27px;border:1px solid #ccc;border-radius:50%}
</style>
</head>
<body>

<div class="abs topbar">
  <div class="abs contact" style="left:132px">
    <svg width="14" height="14" viewBox="0 0 24 24"><path d="M6.6 10.8a15 15 0 0 0 6.6 6.6l2.2-2.2c.3-.3.7-.4 1-.2 1.1.4 2.3.6 3.6.6.6 0 1 .4 1 1V20c0 .6-.4 1-1 1A17 17 0 0 1 3 4c0-.6.4-1 1-1h3.5c.6 0 1 .4 1 1 0 1.3.2 2.5.6 3.6.1.3 0 .7-.2 1z" fill="#222"/></svg>
    555-013-4821
  </div>
  <div class="abs contact" style="left:275px">
    <svg width="15" height="11" viewBox="0 0 16 11"><rect width="16" height="11" fill="#222"/><path d="M0 0l8 6 8-6" stroke="#fff" fill="none"/></svg>
    info@meadowlarkcs.example
  </div>
  <div class="abs quote-btn">Request A Quote</div>
</div>

<div class="abs brand">Meadowlark</div>
<div class="abs social" style="left:880px"></div>
<div class="abs social" style="left:929px"></div>
<div class="abs social" style="left:979px"></div>
<div class="abs social" style="left:1029px"></div>

<nav class="abs nav">
  <div class="abs nav-item active" style="left:132px;width:128px">Home</div>
  <div class="abs nav-item" style="left:260px;width:200px">Services</div>
  <div class="abs nav-div" style="left:460px"></div>
  <div class="abs nav-item" style="left:460px;width:196px">Estimate</div>
  <div class="abs nav-div" style="left:656px"></div>
  <div class="abs nav-item" style="left:656px;width:225px">Testimonials</div>
  <div class="abs nav-div" style="left:881px"></div>
  <div class="abs nav-item" style="left:881px;width:214px">Contact Us</div>
</nav>

<div class="abs hero" role="img" aria-label="Smiling cleaner in yellow gloves wiping a bright white kitchen"></div>
<div class="abs hero-caption">
  <h1>We are local, family-owned, client-focused house and office cleaning company</h1>
  <div class="dots"><span></span><span></span><span></span><span class="on"></span></div>
</div>

<section class="abs welcome">
  <h2>Welcome To Meadowlark Cleaning Services</h2>
  <div class="rule"></div>
  <p>Lorem ipsum dolor sit amet, consectetuer adipiscing elit, sed diam nonummy nibh euismod tincidunt ut laoreet dolore magna aliquam erat volutpat. Ut wisi enim ad minim veniam, quis nostrud exerci tation ullamcorper suscipit lobortis nisl ut aliquip ex ea commodo consequat Duis autem vel eum iriure dolor in hendrerit in vulputate velit esse molestie consequat. autem vel eum iriure dolor in hendrerit in vulputate velit esse molestie consequat, vel illum dolo</p>
  <div class="read-more">Read More</div>
  <svg class="seal" width="228" height="228" viewBox="0 0 228 228" role="img" aria-label="Satisfaction guarantee seal">
    <circle cx="114" cy="114" r="110" fill="none" stroke="var(--blue-light)" stroke-width="5"/>
    <circle cx="114" cy="114" r="94" fill="none" stroke="var(--blue-light)" stroke-width="2"/>
  </svg>
</section>

<section class="abs services">
  <h2 class="abs section-title" style="top:34px">Our Services</h2>
  <div class="abs center-rule" style="left:134px;top:92px;width:930px"></div>

  <div class="abs svc-icon" style="left:158px;top:125px"><svg width="34" height="34" viewBox="0 0 34 34"><rect x="5" y="4" width="16" height="26" fill="none" stroke="#fff" stroke-width="2"/><rect x="21" y="14" width="9" height="16" fill="none" stroke="#fff" stroke-width="2"/><path d="M9 9h3M14 9h3M9 14h3M14 14h3M9 19h3M14 19h3" stroke="#fff" stroke-width="2"/></svg></div>
  <div class="abs svc-title" style="left:260px;top:126px">Office Cleaning</div>
  <div class="abs svc-desc" style="left:260px;top:165px">Duis autem vel eum iriure dolor in hendre Ut wisi enim ad minim veniam.</div>

  <div class="abs svc-icon" style="left:646px;top:125px"><svg width="36" height="30" viewBox="0 0 36 30"><path d="M4 22a14 14 0 0 1 28 0z" fill="#fff"/><rect x="2" y="22" width="32" height="4" fill="#fff"/></svg></div>
  <div class="abs svc-title" style="left:748px;top:126px">Builder Cleaning</div>
  <div class="abs svc-desc" style="left:748px;top:165px">Duis autem vel eum iriure dolor in hendre Ut wisi enim ad minim veniam.</div>

  <div class="abs svc-icon" style="left:158px;top:238px"><svg width="34" height="32" viewBox="0 0 34 32"><path d="M17 2L2 16h5v14h20V16h5z" fill="#fff"/><rect x="14" y="20" width="6" height="10" fill="#2a2a2a"/></svg></div>
  <div class="abs svc-title" style="left:260px;top:239px">Home Cleaning</div>
  <div class="abs svc-desc" style="left:260px;top:278px">Duis autem vel eum iriure dolor in hendre Ut wisi enim ad minim veniam.</div>

  <div class="abs svc-icon" style="left:646px;top:238px"><svg width="36" height="32" viewBox="0 0 36 32"><path d="M4 28L12 14h12l8 14z" fill="#fff"/><path d="M18 2l2 5 5 1-5 2-2 5-2-5-5-2 5-1z" fill="#fff"/></svg></div>
  <div class="abs svc-title" style="left:748px;top:239px">Floor Cleaning</div>
  <div class="abs svc-desc" style="left:748px;top:278px">Duis autem vel eum iriure dolor in hendre Ut wisi enim ad minim veniam.</div>

  <div class="abs svc-icon" style="left:158px;top:352px"><svg width="34" height="34" viewBox="0 0 34 34"><path d="M6 26l14-14M18 6l10 10" stroke="#fff" stroke-width="4"/><circle cx="24" cy="26" r="4" fill="#fff"/></svg></div>
  <div class="abs svc-title" style="left:260px;top:353px">Window Cleaning</div>
  <div class="abs svc-desc" style="left:260px;top:392px">Duis autem vel eum iriure dolor in hendre Ut wisi enim ad minim veniam.</div>

  <div class="abs svc-icon" style="left:646px;top:352px"><svg width="34" height="34" viewBox="0 0 34 34"><path d="M8 26V14a8 8 0 0 1 16 0" fill="none" stroke="#fff" stroke-width="3"/><rect x="4" y="24" width="10" height="6" fill="#fff"/><circle cx="24" cy="26" r="5" fill="none" stroke="#fff" stroke-width="3"/></svg></div>
  <div class="abs svc-title" style="left:748px;top:353px">Other Cleaning</div>
  <div class="abs svc-desc" style="left:748px;top:392px">Duis autem vel eum iriure dolor in hendre Ut wisi enim ad minim veniam.</div>
</section>

<h2 class="abs section-title" style="top:1572px">See What Clients Have To Say About Us</h2>
<div class="abs center-rule" style="left:127px;top:1625px;width:931px"></div>

<div class="abs arrow" style="left:62px"><svg width="10" height="14" viewBox="0 0 10 14"><path d="M8 1L2 7l6 6" stroke="#111" stroke-width="3" fill="none"/></svg></div>
<div class="abs arrow" style="left:1100px"><svg width="10" height="14" viewBox="0 0 10 14"><path d="M2 1l6 6-6 6" stroke="#111" stroke-width="3" fill="none"/></svg></div>

<div class="abs card" style="left:132px"><h4>Lorem ipsum dolor</h4><p>“ Lorem ipsum dolor sit amet, sed jnfkvjbnig consectetuer adipiscing elit, sed diamggi. nonummy nibh euismod tincidunt uthjh elit laoreet dolore magna aliquam eratghs. ”</p></div>
<div class="abs card" style="left:455px"><h4>Lorem ipsum dolor</h4><p>“ Lorem ipsum dolor sit amet, sed jnfkvjbing consectetuer adipiscing elit, sed diamgmi. nonummy nibh euismod tincidunt uthjho elit laoreet dolore magna aliquam eratghs. ”</p></div>
<div class="abs card" style="left:778px"><h4>Lorem ipsum dolor</h4><p>“ Lorem ipsum dolor sit amet, sed jnfkvjbni consectetuer adipiscing elit, sed diamgm. nonummy nibh euismod tincidunt uthjho elit laoreet dolore magna aliquam eratghs. ”</p></div>
<div class="abs avatar" style="left:244px" role="img" aria-label="Client portrait"></div>
<div class="abs avatar" style="left:567px" role="img" aria-label="Client portrait"></div>
<div class="abs avatar" style="left:890px" role="img" aria-label="Client portrait"></div>

<footer class="abs footer">
  <div class="abs f-head" style="left:133px;width:120px">Quick Links</div>
  <ul class="abs f-links">
    <li>Home</li><li>Services</li><li>Estimate</li><li>Testimonials</li><li>Contact Us</li>
  </ul>
  <div class="abs f-sep" style="left:296px"></div>

  <div class="abs f-head" style="left:322px;width:222px">Contact Information</div>
  <div class="abs f-line" style="left:322px;top:62px">
    <svg width="10" height="14" viewBox="0 0 10 14"><path d="M5 0a5 5 0 0 1 5 5c0 4-5 9-5 9S0 9 0 5a5 5 0 0 1 5-5z" fill="var(--blue)"/><circle cx="5" cy="5" r="2" fill="var(--footer)"/></svg>
    <div style="line-height:17px"><b>Meadowlark Cleaning Services</b><br>123 euismod cidun utwsf<br>laok re etmok larwmdw</div>
  </div>
  <div class="abs f-line" style="left:322px;top:134px;font-weight:700">
    <svg width="13" height="13" viewBox="0 0 24 24"><path d="M6.6 10.8a15 15 0 0 0 6.6 6.6l2.2-2.2c.3-.3.7-.4 1-.2 1.1.4 2.3.6 3.6.6.6 0 1 .4 1 1V20c0 .6-.4 1-1 1A17 17 0 0 1 3 4c0-.6.4-1 1-1h3.5c.6 0 1 .4 1 1 0 1.3.2 2.5.6 3.6.1.3 0 .7-.2 1z" fill="var(--blue)"/></svg>
    555-013-4821
  </div>
  <div class="abs f-line" style="left:322px;top:176px">
    <svg width="13" height="10" viewBox="0 0 16 11"><rect width="16" height="11" fill="var(--blue)"/><path d="M0 0l8 6 8-6" stroke="var(--footer)" fill="none"/></svg>
    info@meadowlarkcs.example
  </div>
  <div class="abs f-sep" style="left:558px"></div>

  <div class="abs f-head" style="left:580px;width:232px">Location Map</div>
  <div class="abs map" role="img" aria-label="Street map showing the office location"></div>
  <div class="abs f-sep" style="left:844px"></div>

  <div class="abs f-brand">Meadowlark</div>
</footer>

<div class="abs bottombar">
  <div class="abs" style="left:132px;top:12px">Copyright © 2016 Meadowlark Cleaning Services.  All Right Reserved.</div>
  <div class="abs f-social" style="left:930px"></div>
  <div class="abs f-social" style="left:967px"></div>
  <div class="abs f-social" style="left:1004px"></div>
  <div class="abs f-social" style="left:1041px"></div>
</div>

</body>
</html>
```